Award-winnning Estate Agent needs a premium version of their 'For Sale' board design

We need a premium option for our 'For Sale' board design. We have a standard board that is attached to this brief, but were are looking to have a premium design version that we will use when selling exclusive properties. Our company name is Harbour Lane Estates and the name for this is exclusive selection is: 'The Harbour Collection'. The design needs to work with our current brand, but have a distinctive PREMIUM feel to it. I have uploaded the barnd guidelines and also some of the exisisting logo variations. We do NOT need a new logo but feel free to play around with colours, fonts, sizes etc. for the sign.

Target Market(s)

Property buyers & house hunters

Industry/Entity Type

Real Estate - Residential Property

Font styles to use
Sans Serif

Requirements
Must have
• A premium fee, must be square design, must be easy to read when driving past the sign
Nice to have
• I'm open ot ideas

```html
<!DOCTYPE html>
<html lang="en">
<head>
<meta charset="utf-8">
<title>Harbour Lane Estates – For Sale Board</title>
<link href="https://fonts.googleapis.com/css2?family=Roboto:wght@500;700;900&display=swap" rel="stylesheet">
<style>
  :root {
    --brand-purple: #3a2a72;
    --brand-blue: #1b75bc;
    --brand-sky: #27a9e1;
    --board-white: #ffffff;
    --footer-mist: #eef1f7;
    --photo-roof: #a8705e;
    --photo-lawn: #6e9a4a;
    --photo-stone: #cfc6b4;
  }
  * { margin: 0; padding: 0; box-sizing: border-box; }
  html, body { width: 1200px; height: 1200px; overflow: hidden; background: var(--board-white); }
  body { font-family: "Roboto", Arial, sans-serif; }
  .board { position: relative; width: 1200px; height: 1200px; background: var(--board-white); overflow: hidden; }
  .board-art { position: absolute; inset: 0; }
  .brand {
    position: absolute; left: 76px; top: 70px; width: 300px;
    display: flex; flex-direction: column; align-items: center; gap: 22px;
  }
  .brand-mark { width: 84px; height: 84px; background: var(--brand-blue); }
  .brand-name { font-size: 30px; font-weight: 500; color: var(--brand-purple); white-space: nowrap; }
  .collection-title {
    position: absolute; left: 74px; top: 440px;
    color: var(--brand-purple); font-weight: 700; line-height: 1;
  }
  .collection-title .lead { display: block; font-size: 116px; letter-spacing: -2px; }
  .collection-title .line-one { display: block; font-size: 74px; margin-top: 20px; }
  .collection-title .line-two { display: block; font-size: 80px; margin-top: 12px; }
  .sale-band {
    position: absolute; left: 0; top: 769px; width: 1200px; height: 244px;
    background: var(--brand-blue);
    display: flex; align-items: center;
  }
  .sale-word {
    padding-left: 80px; color: var(--board-white);
    font-size: 278px; font-weight: 700; line-height: 1; letter-spacing: -2px;
    margin-top: 8px;
  }
  .contact { position: absolute; left: 78px; top: 1026px; display: flex; align-items: center; gap: 22px; }
  .contact-icon { width: 92px; height: 92px; }
  .contact-numbers { color: var(--brand-purple); font-weight: 700; font-size: 46px; line-height: 45px; letter-spacing: 0.5px; }
  .web-address {
    position: absolute; right: 82px; top: 1080px;
    color: var(--brand-blue); font-size: 31px; font-weight: 500;
  }
  .footer-strip { position: absolute; left: 0; bottom: 0; width: 1200px; height: 59px; background: var(--footer-mist); }
</style>
</head>
<body>
<main class="board">
  <svg class="board-art" width="1200" height="1200" viewBox="0 0 1200 1200" aria-hidden="false">
    <defs>
      <linearGradient id="propertyTones" x1="0" y1="0" x2="0" y2="1">
        <stop offset="0" stop-color="#8fae6a"/>
        <stop offset="0.25" stop-color="var(--photo-roof)"/>
        <stop offset="0.55" stop-color="var(--photo-stone)"/>
        <stop offset="0.8" stop-color="var(--photo-lawn)"/>
        <stop offset="1" stop-color="#b49584"/>
      </linearGradient>
    </defs>
    <path class="wave-deep" d="M372 0 C388 430 700 762 1200 752 L1200 0 Z" fill="#1b75bc"/>
    <path class="wave-light" d="M380 0 C398 390 700 706 1200 692 L1200 0 Z" fill="#27a9e1"/>
    <path class="property-photo" role="img" aria-label="Aerial photograph of a detached stone house with a tiled roof, double garage, lawn and paved driveway"
          d="M388 0 C410 350 720 628 1200 612 L1200 0 Z" fill="url(#propertyTones)"/>
  </svg>

  <div class="brand">
    <span class="brand-mark"></span>
    <span class="brand-name">Harbour Lane Estates</span>
  </div>

  <h1 class="collection-title">
    <span class="lead">The</span>
    <span class="line-one">HARBOUR</span>
    <span class="line-two">COLLECTION</span>
  </h1>

  <div class="sale-band"><span class="sale-word">For Sale</span></div>

  <div class="contact">
    <svg class="contact-icon" viewBox="0 0 92 92" aria-hidden="true">
      <circle cx="46" cy="46" r="46" fill="#3a2a72"/>
      <path d="M33 24c2-1 4 0 5 2l4 8c1 2 0 4-1 5l-3 3c2 5 6 9 11 11l3-3c1-1 3-2 5-1l8 4c2 1 3 3 2 5l-2 5c-1 2-3 3-5 3C43 63 29 49 28 32c0-2 1-4 3-5z" fill="#ffffff"/>
    </svg>
    <div class="contact-numbers">
      <div>01632 960412</div>
      <div>07700 900318</div>
    </div>
  </div>

  <div class="web-address">www.harbourlaneestates.co.uk</div>

  <div class="footer-strip"></div>
</main>
</body>
</html>
```